Brisbane IT support business needs our first letterhead (Contest)

Hello we are a Brisbane based Information Technology company providing support and services to small and medium sized businesses. We provide a range of services and solutions.

The business name is Harlowe Network Computing Services, or HNCS for short.

I am looking for a letterhead that looks professional (don't we all want that), but most importantly, it most utilize the colours in the logo attached, and any text used preferably in font type: HandelGotDBol.

```html
<!DOCTYPE html>
<html lang="en">
<head>
<meta charset="utf-8">
<title>Harlowe Network Computing Services Letterhead</title>
<link href="https://fonts.googleapis.com/css2?family=Oxanium:wght@500;600;700&display=swap" rel="stylesheet">
<style>
  :root {
    --backdrop: #e4e4e4;
    --paper: #ffffff;
    --brand-band: #044a66;
    --brand-white: #ffffff;
    --ink: #161616;
    --mark-faint: #e6edf1;
    --signature-tint: #eef2f8;
  }
  * { box-sizing: border-box; margin: 0; padding: 0; }
  html, body {
    width: 878px;
    height: 1200px;
    overflow: hidden;
    background: var(--backdrop);
    font-family: "Oxanium", "Segoe UI", sans-serif;
  }
  .letterhead {
    position: absolute;
    left: 57px;
    top: 60px;
    width: 764px;
    height: 1080px;
    background: var(--paper);
    box-shadow: 0 2px 10px rgba(0,0,0,0.12);
    overflow: hidden;
  }
  .brand-band {
    height: 145px;
    background: var(--brand-band);
    display: flex;
    align-items: center;
    justify-content: center;
    gap: 14px;
  }
  .brand-square {
    width: 16px;
    height: 16px;
    background: var(--brand-white);
  }
  .brand-name {
    color: var(--brand-white);
    font-size: 26px;
    font-weight: 700;
    letter-spacing: 0.5px;
  }
  .watermark {
    position: absolute;
    left: 0;
    right: 0;
    top: 560px;
    text-align: center;
    font-size: 44px;
    font-weight: 700;
    color: var(--mark-faint);
    pointer-events: none;
  }
  .letter {
    position: absolute;
    left: 99px;
    top: 340px;
    width: 568px;
    color: var(--ink);
  }
  .salutation {
    font-size: 23px;
    font-weight: 700;
    margin-bottom: 42px;
  }
  .letter-body p {
    font-size: 13.4px;
    font-weight: 600;
    line-height: 20.5px;
    text-align: justify;
    margin-bottom: 20.5px;
  }
  .signature {
    position: absolute;
    right: 96px;
    top: 848px;
    width: 118px;
    height: 46px;
    background: var(--signature-tint);
    border-radius: 4px;
  }
</style>
</head>
<body>
  <main class="letterhead">
    <header class="brand-band">
      <div class="brand-square"></div>
      <div class="brand-name">Harlowe Network Computing Services</div>
    </header>

    <div class="watermark" aria-hidden="true">Harlowe Network Computing Services</div>

    <section class="letter">
      <h1 class="salutation">Dear Mr. Smith,</h1>
      <div class="letter-body">
        <p>Lorem ipsum dolor sit amet, consectetur adipiscing elit. Donec orci purus, luctus vitae dignissim eu, iaculis sed purus. Vivamus faucibus, ipsum nec aliquet viverra, leo mauris condimentum ligula, sit amet sagittis enim ligula quis arcu. Nam egestas tortor id nisi porttitor mattis. In tortor ante, ultricies in suscipit a, tempus non massa. Vivamus et auctor mi. Fusce vel massa nulla. Phasellus nec eros mauris, et scelerisque orci.</p>
        <p>Donec malesuada orci vitae nulla accumsan porta a id massa. Quisque accumsan iaculis magna sit amet fringilla. Maecenas consequat, magna eget tincidunt semper, odio nibh rutrum mi, id feugiat ante nisi eu risus. Vestibulum nunc orci, rhoncus a placerat in, ultricies in mi. Cras mattis varius eros, vel fringilla nisi suscipit eget. Quisque scelerisque sagittis nulla at porttitor.</p>
        <p>Sed id augue vitae urna euismod commodo aliquet a quam. Pellentesque arcu velit, cursus et malesuada ut, consequat et diam. Nullam erat sem, rhoncus id ullamcorper vitae, rhoncus et arcu. In ultricies ultricies nulla, ut rutrum nisi iaculis at. Donec eu magna a metus ornare faucibus. Fusce aliquet faucibus ultricies. Morbi semper, est id tincidunt gravida, sem arcu adipiscing lacus, ac bibendum nulla leo eu purus. Quisque nec diam sed risus consectetur a ccumsan quis quis nibh. Vestibulum id purus lorem.</p>
      </div>
    </section>

    <div class="signature" role="img" aria-label="Handwritten signature of the sender"></div>
  </main>
</body>
</html>
```